Criação de Papelaria Profissional para Advocacia e Direito
A empresa queria:
" Escritório com atuação perante empresários. Trabalhamos com assessoria jurídica para empresas em mais de 3 estados. "

```html
<!DOCTYPE html>
<html lang="pt-BR">
<head>
<meta charset="utf-8">
<title>Assinatura de e-mail — Almeida &amp; Toledo</title>
<link rel="stylesheet" href="https://fonts.googleapis.com/css2?family=Montserrat:wght@400;500;600&display=swap">
<style>
  :root {
    --page: #eeeeee;
    --band: #141414;
    --ring: #ffffff;
    --text: #ffffff;
    --muted: #b9b9b9;
    --rule: #6a6a6a;
    --photo-light: #e9e7e4;
    --photo-mid: #b8b2ab;
  }
  * { box-sizing: border-box; margin: 0; padding: 0; }
  html, body { width: 1200px; height: 1200px; overflow: hidden; }
  body {
    background: var(--page);
    font-family: "Montserrat", sans-serif;
    display: flex; align-items: center; justify-content: center;
  }
  .signature {
    position: relative;
    width: 1100px; height: 264px;
    background: var(--band);
    border-radius: 132px;
    display: flex; align-items: center;
    padding-left: 18px;
    color: var(--text);
  }
  .portrait {
    width: 228px; height: 228px; border-radius: 50%;
    background: var(--ring); padding: 8px; flex: none;
  }
  .portrait-fill {
    width: 100%; height: 100%; border-radius: 50%;
    background: radial-gradient(circle at 50% 40%, var(--photo-mid) 0%, var(--photo-light) 70%);
  }
  .divider { width: 2px; height: 150px; background: var(--rule); flex: none; }
  .divider--left { margin-left: 34px; }
  .brand {
    display: flex; align-items: center; gap: 18px;
    padding: 0 34px; flex: none;
  }
  .brand-mark { width: 26px; height: 26px; background: var(--text); flex: none; }
  .brand-name {
    font-weight: 500; font-size: 30px; line-height: 1.15;
    letter-spacing: 2px; text-transform: uppercase;
  }
  .contact { padding-left: 34px; flex: 1; }
  .person-name { font-size: 25px; font-weight: 500; letter-spacing: .5px; }
  .person-reg { font-size: 14px; color: var(--muted); margin-top: 4px; letter-spacing: 1px; }
  .contact-line {
    font-size: 15px; color: var(--muted); margin-top: 10px;
    display: flex; align-items: center; gap: 8px;
  }
  .contact-grid {
    display: grid; grid-template-columns: auto auto; column-gap: 36px;
    margin-top: 26px; font-size: 14px; color: var(--muted); line-height: 1.6;
  }
  .contact-web { text-align: left; }
  .social { display: flex; align-items: center; gap: 8px; }
  .social-dot { width: 11px; height: 11px; border-radius: 50%; background: var(--text); }
  .phone-icon { width: 16px; height: 16px; flex: none; }
</style>
</head>
<body>
  <section class="signature">
    <div class="portrait">
      <div class="portrait-fill" role="img" aria-label="Retrato do advogado, fundo claro"></div>
    </div>
    <div class="divider divider--left"></div>
    <div class="brand">
      <span class="brand-mark"></span>
      <span class="brand-name">Almeida<br>&amp; Toledo</span>
    </div>
    <div class="divider"></div>
    <div class="contact">
      <p class="person-name">Rogério Almeida</p>
      <p class="person-reg">OAB AL 10477</p>
      <p class="contact-line">
        <svg class="phone-icon" viewBox="0 0 24 24" aria-hidden="true">
          <path d="M6.6 10.8a15 15 0 0 0 6.6 6.6l2.2-2.2c.3-.3.7-.4 1-.2 1.1.4 2.3.6 3.6.6.6 0 1 .4 1 1V20c0 .6-.4 1-1 1C10.6 21 3 13.4 3 4c0-.6.4-1 1-1h3.5c.6 0 1 .4 1 1 0 1.3.2 2.5.6 3.6.1.3 0 .7-.2 1z" fill="#ffffff"/>
        </svg>
        67 3100 4480
      </p>
      <p class="contact-line">rogerio@almeidaetoledo.com.br</p>
      <div class="contact-grid">
        <span>Rua Vicente Sales, S/N</span>
        <span class="social"><span class="social-dot"></span>@almeidaetoledo</span>
        <span>Penedo - AL - 57200000</span>
        <span class="contact-web">www.almeidaetoledo.com.br</span>
      </div>
    </div>
  </section>
</body>
</html>
```